Fizzle Puddle Crew - Goop Guild - Shopify Website Design

A monthly subscription company. Need a Shopify Website Design and uploaded to fully work with Brisk Renewals.

Please look at these sites for examples as well as the images I enclosed.

https://www.mochigoopworks.example/
https://purelandroot.example/
https://www.renewa-ol.example/
https://www.pantrypop.example/
https://www.globalnibbles.example/
https://www.sipmarket.example/
https://grindcrate.example/

Number of Pages Required

1 page

```html
<!DOCTYPE html>
<html lang="en">
<head>
<meta charset="utf-8">
<title>Fizzle Puddle Crew – Goop Guild</title>
<link href="https://fonts.googleapis.com/css2?family=Rubik:wght@500;700&family=Roboto:wght@400;500;700&family=Roboto+Slab:wght@300;400&display=swap" rel="stylesheet">
<style>
:root{
  --rose:#f2707f;
  --rose-deep:#e85f6f;
  --blush:#f4a3b1;
  --ink:#2b2b2b;
  --muted:#6a6a6a;
  --line:#d8d8d8;
  --night:#141414;
  --white:#ffffff;
}
*{margin:0;padding:0;box-sizing:border-box}
html,body{width:1200px;height:4926px;overflow:hidden}
body{position:relative;background:var(--white);font-family:"Roboto",sans-serif;color:var(--ink)}
.abs{position:absolute}
.topbar{left:0;top:0;width:1200px;height:38px;background:var(--rose);color:var(--white);font-size:11px;font-weight:500;z-index:3}
.topbar span{position:absolute;top:12px}
.topbar .promo{left:0;width:1200px;text-align:center;font-size:13px;font-weight:700;top:11px}
.hero{left:0;top:38px;width:1200px;height:715px;background:radial-gradient(circle at 70% 40%,#e33fd0 0%,#9a2be0 35%,#3b2fc9 65%,#1c2aa8 100%)}
.logo{left:40px;top:64px;font-family:"Rubik",sans-serif;font-weight:500;font-size:30px;color:var(--white);letter-spacing:1px}
.nav a{position:absolute;top:78px;transform:translateX(-50%);font-size:13px;font-weight:700;color:var(--white);text-decoration:none}
.nav a.active{text-decoration:underline}
.hero-title{left:54px;top:262px;font-family:"Rubik",sans-serif;font-weight:700;font-size:58px;line-height:60px;color:var(--white)}
.hero-copy{left:54px;top:396px;width:300px;font-family:"Roboto Slab",serif;font-weight:300;font-size:17px;line-height:23px;color:var(--white)}
.btn{display:flex;align-items:center;justify-content:center;background:var(--rose);color:var(--white);font-size:12px;font-weight:700;text-transform:uppercase;border-radius:3px}
.dot{width:16px;height:16px;border:2px solid var(--white);border-radius:50%;top:668px}
.dot.on{background:var(--rose);border-color:var(--rose)}
.section-title{left:0;width:1200px;text-align:center;font-family:"Rubik",sans-serif;font-weight:500;font-size:34px;color:var(--ink)}
.rule{left:566px;width:68px;height:3px;background:var(--rose)}
.tile{display:flex;flex-direction:column;align-items:center;justify-content:center;color:var(--white);text-align:center}
.tile h3{font-family:"Rubik",sans-serif;font-weight:500;font-size:19px;letter-spacing:.5px}
.tile i{display:block;width:52px;height:3px;background:var(--white);margin:12px 0}
.tile p{font-family:"Roboto Slab",serif;font-weight:300;font-size:14px;line-height:20px;width:170px}
.photo{border-radius:0}
.welcome-sub{font-family:"Rubik",sans-serif;font-weight:500;font-size:28px;line-height:36px}
.body-copy{font-family:"Roboto Slab",serif;font-weight:300;font-size:14px;line-height:22px;color:var(--muted)}
.card{border:2px solid var(--line);background:var(--white)}
.card .img{position:absolute;left:8px;top:8px;right:8px;height:170px}
.card .btn{position:absolute;left:8px;right:8px;top:189px;height:37px}
.card .name{position:absolute;left:0;right:0;top:250px;text-align:center;font-size:13px;line-height:22px}
.price{color:var(--rose);font-size:14px}
.card .price{position:absolute;left:0;right:0;top:303px;text-align:center}
.arrow{width:26px;height:26px;border:1px solid #777;border-radius:50%}
.banner{left:0;top:2608px;width:1200px;height:528px;background:linear-gradient(100deg,#f1e530 0%,#ee3a9a 25%,#2fb3e6 45%,#b9b6c8 62%,#f29a3a 78%,#2bb39a 100%)}
.banner-shade{left:0;top:2608px;width:1200px;height:528px;background:linear-gradient(180deg,rgba(90,90,95,0) 30%,rgba(110,110,120,.75) 70%)}
.banner-title{left:0;top:2938px;width:1200px;text-align:center;font-family:"Rubik",sans-serif;font-weight:500;font-size:48px;color:var(--white);letter-spacing:1px}
.box-item .frame{position:absolute;left:0;top:0;width:213px;height:219px;border:2px solid var(--line)}
.box-item .tub{position:absolute;left:40px;top:30px;width:130px;height:160px;border-radius:12px}
.box-item .name{position:absolute;left:0;top:242px;font-size:14px;line-height:21px;width:220px}
.box-item .price{position:absolute;left:0;top:293px}
.box-item .btn{position:absolute;left:0;top:328px;width:134px;height:37px}
.coupon{left:0;top:4374px;width:1200px;height:56px;background:var(--blush);color:var(--white);font-size:12px;font-weight:500;display:flex;align-items:center;justify-content:center}
.footer{left:0;top:4430px;width:1200px;height:496px;background:var(--night);color:#cfcfcf}
.footer h4{position:absolute;top:85px;font-family:"Rubik",sans-serif;font-weight:500;font-size:17px;color:var(--white)}
.footer ul{position:absolute;top:128px;list-style:none;font-size:13px;line-height:27px}
.foot-copy{font-family:"Roboto Slab",serif;font-weight:300;font-size:12px;line-height:21px}
.field{left:847px;top:189px;width:271px;height:36px;background:var(--white);border-radius:18px;color:#888;font-size:11px;padding:12px 18px}
.divider{left:0;top:357px;width:1200px;height:1px;background:#2c2c2c}
.card-mark{top:410px;width:36px;height:26px;background:#3a3f6e;border-radius:3px}
</style>
</head>
<body>

<header>
  <div class="abs topbar">
    <span style="left:38px"><svg width="11" height="11" viewBox="0 0 12 12"><circle cx="5" cy="5" r="3.8" fill="none" stroke="#fff" stroke-width="1.6"/><line x1="8" y1="8" x2="11" y2="11" stroke="#fff" stroke-width="1.8"/></svg></span>
    <span style="left:64px">SEARCH PRODUCTS...</span>
    <span class="promo">FREE DOMESTIC SHIPPING OVER $50</span>
    <span style="left:962px"><svg width="13" height="13" viewBox="0 0 14 14"><circle cx="7" cy="4.5" r="3" fill="none" stroke="#fff" stroke-width="1.4"/><path d="M1.5 13.5c0-3 2.5-4.5 5.5-4.5s5.5 1.5 5.5 4.5" fill="none" stroke="#fff" stroke-width="1.4"/></svg></span>
    <span style="left:985px">SIGN IN/JOIN</span>
    <span style="left:1094px;top:9px"><svg width="20" height="17" viewBox="0 0 20 17"><path d="M1 2h3l2.5 9h10l2-7H6" fill="none" stroke="#fff" stroke-width="1.5"/><circle cx="8" cy="14.5" r="1.4" fill="#fff"/><circle cx="15" cy="14.5" r="1.4" fill="#fff"/></svg></span>
    <span style="left:1124px">CART 0</span>
  </div>
  <div class="abs hero" role="img" aria-label="Tray of slime-making supplies with glitter and beads on colourful bubbly goo"></div>
  <div class="abs logo">Fizzle Puddle Crew</div>
  <nav class="nav">
    <a class="active" style="left:485px">HOME</a>
    <a style="left:604px">CATEGORIES</a>
    <a style="left:740px">OUR SHOP</a>
    <a style="left:862px">ABOUT US</a>
    <a style="left:984px">DELIVERY</a>
    <a style="left:1116px">CONTACT US</a>
  </nav>
  <h1 class="abs hero-title">Fizzle Puddle<br>Crew</h1>
  <p class="abs hero-copy">Sed ut perspiciatis unde omnis iste natus error sit voluptatem accusantium doloremque</p>
  <a class="abs btn" style="left:54px;top:491px;width:130px;height:37px">Shop Now</a>
  <div class="abs dot" style="left:538px"></div>
  <div class="abs dot" style="left:565px"></div>
  <div class="abs dot on" style="left:592px"></div>
  <div class="abs dot" style="left:619px"></div>
  <div class="abs dot" style="left:646px"></div>
</header>

<section>
  <h2 class="abs section-title" style="top:822px">Shop by Collection</h2>
  <div class="abs rule" style="top:881px"></div>
  <div class="abs tile" role="img" aria-label="Slime supplies with a blue splash" style="left:145px;top:930px;width:295px;height:385px;background:linear-gradient(135deg,#e85bb0,#3547d6 50%,#6b3fd0)"><h3>SLIME SUPPLIES</h3><i></i><p>Sed ut perspiciatis unde omnis iste voluptatem accusantium</p></div>
  <div class="abs tile" role="img" aria-label="Pink slime splash with foam beads" style="left:453px;top:930px;width:294px;height:385px;background:linear-gradient(135deg,#f2705a,#e22c8e 50%,#b52ca8)"><h3>SLIME</h3><i></i><p>Sed ut perspiciatis unde omnis iste voluptatem accusantium</p></div>
  <div class="abs tile" role="img" aria-label="Gift tubs of slime with a red splash" style="left:761px;top:930px;width:294px;height:385px;background:linear-gradient(135deg,#f08070,#e5353f 50%,#d0486f)"><h3>FIZZLE PUDDLE GIFTS</h3><i></i><p>Sed ut perspiciatis unde omnis iste voluptatem accusantium</p></div>
</section>

<section>
  <div class="abs photo" role="img" aria-label="Child stretching bright yellow slime" style="left:145px;top:1395px;width:447px;height:464px;background:linear-gradient(120deg,#efe8e0,#f3b23a 50%,#e9e3dc)"></div>
  <div class="abs photo" role="img" aria-label="Hands stretching clear blue slime with snowflake glitter" style="left:619px;top:1395px;width:436px;height:277px;background:linear-gradient(135deg,#5fc9e0,#3fb4d8 55%,#8fd8e8)"></div>
  <p class="abs welcome-sub" style="left:619px;top:1690px;color:var(--ink)">Welcome to</p>
  <p class="abs welcome-sub" style="left:619px;top:1725px;color:var(--rose-deep)">Fizzle Puddle Crew</p>
  <p class="abs body-copy" style="left:619px;top:1776px;width:440px">Sed ut perspiciatis unde omnis iste natus error sit voluptatem accusantium doloremque laudantium, totam rem aperiam, eaque ipsa quae ab illo inventore veritatis et quasi architecto beatae vitae dicta sunt explicabo.</p>
</section>

<section>
  <div class="abs" style="left:34px;top:2052px;width:388px;height:367px;border:2px solid var(--rose)"></div>
  <div class="abs" role="img" aria-label="Slime kit tray on purple bubbly goo" style="left:78px;top:1978px;width:300px;height:516px;background:linear-gradient(160deg,#6a3be0,#3a2fc8 45%,#8d3fd8 75%,#3d2ec5)"></div>
  <h2 class="abs" style="left:700px;top:2018px;width:424px;text-align:right;font-family:'Rubik',sans-serif;font-weight:400;font-size:28px">Featured <span style="font-weight:500">Products</span></h2>
  <div class="abs arrow" style="left:446px;top:2234px"><svg width="24" height="24" viewBox="0 0 24 24"><path d="M14 7l-5 5 5 5" fill="none" stroke="#555" stroke-width="1.5"/></svg></div>
  <div class="abs arrow" style="left:1135px;top:2234px"><svg width="24" height="24" viewBox="0 0 24 24"><path d="M10 7l5 5-5 5" fill="none" stroke="#555" stroke-width="1.5"/></svg></div>
  <div class="abs card" style="left:483px;top:2085px;width:200px;height:336px"><div class="img" role="img" aria-label="Green slime spilling from a tub" style="background:radial-gradient(ellipse at 50% 60%,#7ad83a 0%,#b5ea8a 35%,#fff 65%)"></div><a class="btn">Add to Cart</a><p class="name">Nemo enim ipsam<br>voluptatem quia voluptas</p><p class="price">£148.23</p></div>
  <div class="abs card" style="left:703px;top:2085px;width:200px;height:336px"><div class="img" role="img" aria-label="Red slime spilling from a tub" style="background:radial-gradient(ellipse at 50% 60%,#ee2d55 0%,#f59aae 35%,#fff 65%)"></div><a class="btn">Add to Cart</a><p class="name">Nemo enim ipsam<br>voluptatem quia voluptas</p><p class="price">£148.23</p></div>
  <div class="abs card" style="left:923px;top:2085px;width:201px;height:336px"><div class="img" role="img" aria-label="Pink slime pouring between tubs" style="background:radial-gradient(ellipse at 50% 55%,#f28fc8 0%,#f8c6e2 35%,#fff 65%)"></div><a class="btn">Add to Cart</a><p class="name">Nemo enim ipsam<br>voluptatem quia voluptas</p><p class="price">£148.23</p></div>
</section>

<section>
  <div class="abs banner" role="img" aria-label="Rows of colourful glitter and bead slime"></div>
  <div class="abs banner-shade"></div>
  <h2 class="abs banner-title">SHOP GOOP GUILD</h2>
  <a class="abs btn" style="left:535px;top:3015px;width:130px;height:39px;background:var(--white);color:var(--ink)">Shop Now</a>
</section>

<section>
  <h2 class="abs section-title" style="top:3196px">This Month's Box</h2>
  <div class="abs rule" style="top:3258px"></div>
  <div class="abs box-item" style="left:141px;top:3316px"><div class="frame"><div class="tub" role="img" aria-label="Stacked tubs of red, yellow and green slime" style="background:linear-gradient(180deg,#f04a3a,#f6d800 50%,#55cc2a)"></div></div><p class="name">Nemo enim ipsam<br>voluptatem quia voluptas</p><p class="price">£148.23</p><a class="btn">Add to Cart</a></div>
  <div class="abs box-item" style="left:376px;top:3316px"><div class="frame"><div class="tub" role="img" aria-label="Stacked tubs of blue, purple and red slime" style="background:linear-gradient(180deg,#3a3de0,#b02ad8 50%,#e82d4a)"></div></div><p class="name">Nemo enim ipsam<br>voluptatem quia voluptas</p><p class="price">£148.23</p><a class="btn">Add to Cart</a></div>
  <div class="abs box-item" style="left:610px;top:3316px"><div class="frame"><div class="tub" role="img" aria-label="Stacked tubs of green, teal and blue slime" style="background:linear-gradient(180deg,#3fe05a,#22c9d8 50%,#2a3fd8)"></div></div><p class="name">Nemo enim ipsam<br>voluptatem quia voluptas</p><p class="price">£148.23</p><a class="btn">Add to Cart</a></div>
  <div class="abs box-item" style="left:845px;top:3316px"><div class="frame"><div class="tub" role="img" aria-label="Tubs of pink and orange slime" style="background:linear-gradient(180deg,#f060c8,#f7a0c0 45%,#f79a2a)"></div></div><p class="name">Nemo enim ipsam<br>voluptatem quia voluptas</p><p class="price">£148.23</p><a class="btn">Add to Cart</a></div>
</section>

<section>
  <h2 class="abs section-title" style="top:3771px">What's in a box?</h2>
  <div class="abs tile" role="img" aria-label="Glitter slime with a blue splash" style="left:145px;top:3879px;width:295px;height:386px;background:linear-gradient(135deg,#e04a7a,#3547d6 50%,#c83f5a)"><h3>NEMO ENIM<br>VOLUPTATEM</h3><i></i></div>
  <div class="abs tile" role="img" aria-label="Slime stretched between hands with a green splash" style="left:453px;top:3879px;width:294px;height:386px;background:linear-gradient(135deg,#f1d7c8,#5fcf6a 50%,#e8c0a8)"><h3>NEMO ENIM<br>VOLUPTATEM</h3><i></i></div>
  <div class="abs tile" role="img" aria-label="Dark glitter slime with a magenta splash" style="left:761px;top:3879px;width:294px;height:386px;background:linear-gradient(135deg,#2a2fa8,#d82fc0 50%,#1c1c4a)"><h3>NEMO ENIM<br>VOLUPTATEM</h3><i></i></div>
</section>

<div class="abs coupon">Save 20% when you buy three items with coupon BUYTHREE</div>

<footer class="abs footer">
  <h4 style="left:96px">ABOUT FIZZLE PUDDLE CREW</h4>
  <p class="abs foot-copy" style="left:96px;top:132px;width:300px">Sed ut perspiciatis unde omnis iste natus error sit voluptatem accusantium doloremque laudm, totam rem aperiam, eaque ipsa quae ab illo iventore veritatis et quasi architecto beatae vitae dicta sunt explicabo. Nemo enim ipsam voluptatem quia voluptas sit aspernatur aut odit aut fugit, sed quia consequuntur magni dolores</p>
  <h4 style="left:451px">QUICK LINKS</h4>
  <ul style="left:454px"><li>Terms &amp; Conditions</li><li>Privacy Policy</li><li>Right of Refusal</li><li>Cookies</li><li>Shipping &amp; Delivery Terms</li></ul>
  <h4 style="left:675px">QUICK LINKS</h4>
  <ul style="left:678px"><li>About Us</li><li>Contact Us</li><li>Delivery</li><li>Catalogues</li><li>Shop</li></ul>
  <h4 style="left:847px">SIGN UP FOR NEWSLETTER</h4>
  <p class="abs foot-copy" style="left:847px;top:136px;width:280px">Sed ut perspiciatis unde omnis iste natus error sit voluptatem accusantium</p>
  <div class="abs field">Enter email</div>
  <a class="abs btn" style="left:847px;top:242px;width:137px;height:33px;border-radius:17px">Subscribe</a>
  <div class="abs divider"></div>
  <p class="abs" style="left:101px;top:418px;font-size:12px">Fizzle Puddle Crew © 2020 All Rights Reserved | Privacy Policy | Terms and Conditions</p>
  <div class="abs card-mark" style="left:925px"></div>
  <div class="abs card-mark" style="left:965px;background:#5a5a5a"></div>
  <div class="abs card-mark" style="left:1005px;background:#3d7bc2"></div>
  <div class="abs card-mark" style="left:1045px;background:#8a8a8a"></div>
  <div class="abs card-mark" style="left:1085px;background:#6a6a6a"></div>
</footer>

</body>
</html>
```